Web Design for a Biotech Consulting Firm

We need a web site design for a new business based in Philadelphia called VorentaMx. This is a consulting firm that will serve medical diagnostics industry, which is part of the life science/healthcare industry focusing on developing and marketing products that help in early detection, monitoring or management of diseases. Our consulting firm will help medical diagnostic companies to overcome key challenges in designing, evaluating and marketing new products.Our company name is VorentaMx. Vorenta is Latin word for "something" Dx represents diagnostics. The idea behind the name is that we help companies to transform the original, early product ideas ("nothing") into "something"; which is a product with full clinical utility that will help to improve health and well-being.The web site should use the visual feel of the logo (attached), be modern, simple and clean looking and represent creativity, innovation, scientific thinking and progress.
Updates

Wix Design is acceptable

Industry/Entity Type

Biotechnology

Coding

Coded - Design and coding required

Number of Pages Required

1 page

Font styles to use
Sans Serif

Requirements
Must have
• simple, clean look couple of pages
Should not have
• a lot of pages

```html
<!DOCTYPE html>
<html lang="en">
<head>
<meta charset="utf-8">
<title>VorentaMx — Diagnostics Consulting</title>
<link href="https://fonts.googleapis.com/css2?family=Montserrat:ital,wght@0,400;0,500;0,700;1,400&family=Open+Sans:wght@400;600;700&family=Roboto:wght@300;400;500;700&display=swap" rel="stylesheet">
<style>
:root{
  --blue:#2f8af5;
  --dark:#2b2b2b;
  --ink:#333;
  --grey:#555;
  --light:#f1f1f1;
  --white:#fff;
}
*{box-sizing:border-box;margin:0;padding:0}
html,body{width:1200px;height:3800px;overflow:hidden}
body{position:relative;background:var(--white);font-family:'Roboto',sans-serif;color:var(--ink)}
.abs{position:absolute}
.brand{font-family:'Open Sans',sans-serif;color:var(--ink);font-size:20px;font-weight:400;white-space:nowrap}
.logo-name{left:162px;top:80px}
.nav-line{left:600px;top:75px;width:450px;height:1px;background:var(--blue)}
.nav{left:600px;top:89px;width:450px;display:flex;justify-content:flex-end;gap:30px;font-size:11.5px;font-family:'Open Sans',sans-serif;color:#333}
.hero{left:0;top:257px;width:1200px;height:279px;background:var(--dark)}
.hero-photo{left:0;top:257px;width:1200px;height:279px;background:linear-gradient(120deg,#3b78d8,#6aa7ee 55%,#8fc0f2);clip-path:polygon(650px 0,1200px 0,1200px 279px,550px 279px)}
.bar{height:4px;background:var(--blue)}
.hero-bar{left:171px;top:281px;width:33px}
.hero-title{left:171px;top:308px;color:#fff;font-family:'Open Sans',sans-serif;font-weight:700;font-size:23px;line-height:28px}
.hero-text{left:171px;top:382px;width:340px;color:#fff;font-family:'Open Sans',sans-serif;font-size:13px;line-height:16px}
.btn{background:var(--blue);color:#fff;font-weight:700;display:flex;align-items:center;justify-content:center}
.hero-btn{left:171px;top:480px;width:323px;height:28px;font-size:13px;font-family:'Open Sans',sans-serif}
.card{top:635px;width:280px;height:354px;box-shadow:0 4px 14px rgba(0,0,0,.18);border-radius:4px;overflow:hidden}
.card .photo{position:absolute;inset:0;opacity:.55}
.card .num{position:absolute;left:26px;top:10px;font-family:'Roboto',sans-serif;font-weight:300;font-size:70px;color:#222}
.card .name{position:absolute;left:28px;top:96px;font-size:24px;color:#111}
.card .frame{position:absolute;left:26px;top:156px;width:230px;height:164px;border:3px solid var(--blue);padding:12px 12px;font-family:'Open Sans',sans-serif;font-size:13px;line-height:16px;color:#222}
.card .more{position:absolute;left:14px;bottom:10px;color:var(--blue);font-weight:700;font-size:15px;display:flex;align-items:center;gap:8px}
.insights{left:0;top:1089px;width:1200px;height:451px;background:var(--dark);color:#fff}
.ins-bar{left:469px;top:1133px;width:52px}
.ins-title{left:0;width:1200px;top:1138px;text-align:center;color:var(--blue);font-weight:700;font-size:47px}
.post{top:1232px;width:270px}
.post h3{font-size:24px;line-height:29px;font-weight:700}
.post .date{font-size:16px;margin-top:10px}
.post .rule{height:4px;background:#777;width:250px;margin:12px 0 16px}
.post p{font-size:18px;line-height:22px}
.post p span{color:var(--blue)}
.dots{left:0;top:1463px;width:1200px;border-top:1px dotted #888}
.see-more{left:0;width:1200px;top:1488px;display:flex;justify-content:center;align-items:center;gap:14px;font-weight:700;font-size:17px;color:#fff}
.stat{top:1610px;width:300px;text-align:center}
.stat .n{font-family:'Montserrat',sans-serif;font-weight:700;font-size:100px;color:#575757;line-height:120px}
.stat .r{width:55px;height:4px;background:var(--blue);margin:42px auto 40px}
.stat .l{font-size:23px;color:#555}
.solutions{left:0;top:1878px;width:1200px;height:661px;background:var(--light)}
.sec-bar{width:52px}
.sec-title{font-family:'Montserrat',sans-serif;font-weight:700;font-size:50px;color:#222}
.sec-sub{font-family:'Montserrat',sans-serif;font-style:italic;font-size:14px;color:#444}
.tabs{left:156px;top:2086px;width:297px}
.tab{height:58px;margin-bottom:3px;background:#fff;border:1px solid #ccc;display:flex;align-items:center;gap:24px;padding-left:22px;font-size:16px;color:#333}
.tab.active{background:var(--dark);color:#fff;border-color:var(--dark)}
.panel{left:469px;top:2084px;width:566px;height:410px;background:#fff;padding:88px 50px 0 50px;font-size:15.5px;line-height:22px;color:#444}
.panel .more{margin-top:36px;color:var(--blue);font-weight:700;font-size:13px;display:flex;align-items:center;gap:8px;padding-left:4px}
.pub-text{left:170px;top:2713px;width:860px;text-align:center;font-size:20.5px;line-height:24px;color:#333}
.pub-btn{left:413px;top:2995px;width:355px;height:47px;font-size:18px}
.partner{top:3160px;width:120px;height:76px;background:#c9c9c9;border-radius:6px}
.arrow-l,.arrow-r{top:3185px;font-size:30px;font-weight:700;color:#111}
.footer{left:0;top:3339px;width:1200px;height:461px;background:var(--dark);color:#ddd}
.f-title{font-size:23px;color:#ddd;font-weight:400;font-family:'Montserrat',sans-serif}
.f-text{left:360px;top:3455px;width:335px;text-align:center;font-family:'Montserrat',sans-serif;font-size:17px;line-height:21px}
.f-input{left:387px;top:3540px;width:280px;height:40px;border:3px solid #ccc;display:flex;align-items:center;justify-content:space-between;padding:0 14px;font-family:'Montserrat',sans-serif;font-size:17px}
.f-logo-name{left:150px;top:3560px;color:#fff;font-size:19px}
.contact{left:755px;font-family:'Montserrat',sans-serif;font-size:17px;line-height:21px;display:flex;gap:25px;align-items:flex-start}
.contact svg{flex:none;margin-top:2px}
.social{left:455px;top:3638px;display:flex;gap:18px}
.copyright{left:0;width:1200px;top:3733px;text-align:center;font-family:'Montserrat',sans-serif;font-size:17px}
</style>
</head>
<body>

<header>
  <div class="abs brand logo-name">VorentaMx</div>
  <svg class="abs" style="left:1032px;top:48px" width="18" height="18" viewBox="0 0 18 18" fill="none" stroke="#2f8af5" stroke-width="1.6"><circle cx="7.5" cy="7.5" r="5.5"/><path d="M11.5 11.5l5 5"/></svg>
  <div class="abs nav-line"></div>
  <nav class="abs nav"><span>HOME</span><span>ABOUT</span><span>PRODUCTS</span><span>R&amp;D</span><span>RESPONSIBILITIES</span></nav>
</header>

<section>
  <div class="abs hero"></div>
  <div class="abs hero-photo" role="img" aria-label="Photo of two scientists in a lab working at a microscope, tinted blue"></div>
  <div class="abs bar hero-bar"></div>
  <h1 class="abs hero-title">PLATFORM &amp; SERVICES<br>FOR YOUR MISSION</h1>
  <p class="abs hero-text">Brightquill delivers the most effective combination of technology and services to scholarly and professional publishers, empowering your digital strategy.</p>
  <div class="abs btn hero-btn">Learn More</div>
</section>

<section>
  <article class="abs card" style="left:150px">
    <div class="photo" role="img" aria-label="Photo of a tree beside a stone building" style="background:linear-gradient(160deg,#8e8478,#c9c2b8 60%,#e2ded8)"></div>
    <div class="num">01</div><div class="name">Sed Ut Perspiciatis</div>
    <div class="frame">Sed ut perspiciatis unde omnis iste natus error sit voluptatem accusantium doloremque laudantium, totam rem aper iam, eaque ipsa quae ab illo inventore veritatist
      <div class="more">READ MORE <svg width="20" height="12" viewBox="0 0 20 12" fill="none" stroke="#2f8af5" stroke-width="1.6"><path d="M1 6h17M13 1l5 5-5 5"/></svg></div></div>
  </article>
  <article class="abs card" style="left:455px">
    <div class="photo" role="img" aria-label="Photo of a red brick building facade" style="background:linear-gradient(160deg,#8a4b3a,#b8826f 60%,#cfa797)"></div>
    <div class="num">02</div><div class="name">Omnis Istegry</div>
    <div class="frame">Sed ut perspiciatis unde omnis iste natus error sit voluptatem accusantium doloremque laudantium, totam rem aper iam, eaque ipsa quae ab illo inventore veritatist
      <div class="more">READ MORE <svg width="20" height="12" viewBox="0 0 20 12" fill="none" stroke="#2f8af5" stroke-width="1.6"><path d="M1 6h17M13 1l5 5-5 5"/></svg></div></div>
  </article>
  <article class="abs card" style="left:760px">
    <div class="photo" role="img" aria-label="Photo of glass office towers" style="background:linear-gradient(160deg,#7f9fc7,#b8cde6 60%,#dce7f4)"></div>
    <div class="num">03</div><div class="name">Sit Voluptatem</div>
    <div class="frame">Sed ut perspiciatis unde omnis iste natus error sit voluptatem accusantium doloremque laudantium, totam rem aper iam, eaque ipsa quae ab illo inventore veritatist
      <div class="more">READ MORE <svg width="20" height="12" viewBox="0 0 20 12" fill="none" stroke="#2f8af5" stroke-width="1.6"><path d="M1 6h17M13 1l5 5-5 5"/></svg></div></div>
  </article>
</section>

<section>
  <div class="abs insights"></div>
  <div class="abs bar ins-bar"></div>
  <h2 class="abs ins-title">Our Insights</h2>
  <article class="abs post" style="left:160px;color:#fff"><h3>Neque porro quisquam est qui dolorem ipsum.</h3><div class="date">21 May 2018</div><div class="rule"></div><p>It is a long established fact that a reader will be distracted by the readable content of a page when looking at its layout. <span>Read More.</span></p></article>
  <article class="abs post" style="left:463px;color:#fff"><h3>Neque porro quisquam est qui dolorem ipsum.</h3><div class="date">21 May 2018</div><div class="rule"></div><p>It is a long established fact that a reader will be distracted by the readable content of a page when looking at its layout. <span>Read More.</span></p></article>
  <article class="abs post" style="left:766px;color:#fff"><h3>Neque porro quisquam est qui dolorem ipsum.</h3><div class="date">21 May 2018</div><div class="rule"></div><p>It is a long established fact that a reader will be distracted by the readable content of a page when looking at its layout. <span>Read More.</span></p></article>
  <div class="abs dots"></div>
  <div class="abs see-more"><svg width="20" height="20" viewBox="0 0 20 20" stroke="#fff" stroke-width="2"><path d="M10 1v18M1 10h18"/></svg>SEE MORE</div>
</section>

<section>
  <div class="abs stat" style="left:145px"><div class="n">135+</div><div class="r"></div><div class="l">PROJECTS EVALUATED</div></div>
  <div class="abs stat" style="left:455px"><div class="n">45</div><div class="r"></div><div class="l">STARTUPS LAUNCHED</div></div>
  <div class="abs stat" style="left:745px"><div class="n">8</div><div class="r"></div><div class="l">YEARS OF EXPERIENCE</div></div>
</section>

<section>
  <div class="abs solutions"></div>
  <div class="abs bar sec-bar" style="left:428px;top:1944px"></div>
  <h2 class="abs sec-title" style="left:428px;top:1948px">Our Solutions</h2>
  <div class="abs sec-sub" style="left:428px;top:2007px">that provide value to your business</div>
  <div class="abs tabs">
    <div class="tab active"><span>&#9656;</span>Lorem Ipsum Dolor</div>
    <div class="tab"><span>&#9656;</span>Eiusmod Tempor</div>
    <div class="tab"><span>&#9656;</span>Eiusmod Tempor</div>
    <div class="tab"><span>&#9656;</span>Eiusmod Tempor</div>
    <div class="tab"><span>&#9656;</span>Eiusmod Tempor</div>
    <div class="tab"><span>&#9656;</span>Eiusmod Tempor</div>
  </div>
  <div class="abs panel">Lorem ipsum dolor sit amet, consectetur adipiscing elit, sed do eiusmod tempor incididunt ut labore et dolore magna aliqua. Ut enim ad minim veniam, quis nostrud exercitation ullamco laboris nisi ut aliquip ex ea commodo consequat. Duis aute irure dolor in reprehenderit in voluptate velit esse cillum dolore eu fugiat nulla pariatur. Excepteur sint occaecat cupidatat non proident, sunt in culpa qui officia deserunt mollit anim id est laborum.
    <div class="more">READ MORE <svg width="16" height="10" viewBox="0 0 16 10" fill="none" stroke="#2f8af5" stroke-width="1.5"><path d="M1 5h13M10 1l4 4-4 4"/></svg></div>
  </div>
</section>

<section>
  <div class="abs bar sec-bar" style="left:423px;top:2592px"></div>
  <h2 class="abs sec-title" style="left:423px;top:2596px">Our Publications</h2>
  <div class="abs sec-sub" style="left:423px;top:2655px">see reports and articles currently available</div>
  <p class="abs pub-text">Sed ut perspiciatis unde omnis iste natus error sit voluptatem accusantium doloremque laudantium, totam rem aperiam, eaque ipsa quae ab illo inventore veritatis et quasi architecto beatae vitae dicta sunt explicabo. Nemo enim ipsam voluptatem quia voluptas sit aspernatur aut odit aut fugit, sed quia consequuntur magni dolores eos qui ratione voluptatem sequi nesciunt. Neque porro quisquam est, qui dolorem ipsum quia dolor sit amet, consectetur, adipisci velit, sed quia non numquam eius modi tempora incidunt ut labore et dolore magnam aliquam quaerat voluptatem. Ut enim ad minima veniam, quis nostrum exercitationem ullam corporis suscipit laboriosam, nisi ut aliquid ex ea commodi consequatur? Quis autem vel eum iure reprehenderit qui in ea voluptate velit esse quam nihil molestiae consequatur, vel illum qui dolorem eum fugiat quo voluptas nulla pariatur</p>
  <div class="abs btn pub-btn">SEE ALL PUBLICATIONS</div>
</section>

<section>
  <div class="abs arrow-l" style="left:64px">&lsaquo;</div>
  <div class="abs partner" style="left:136px"></div>
  <div class="abs partner" style="left:340px"></div>
  <div class="abs partner" style="left:540px"></div>
  <div class="abs partner" style="left:742px"></div>
  <div class="abs partner" style="left:945px"></div>
  <div class="abs arrow-r" style="left:1124px">&rsaquo;</div>
</section>

<footer>
  <div class="abs footer"></div>
  <h3 class="abs f-title" style="left:381px;top:3377px">SUBSCRIBE TO OUR BLOG</h3>
  <h3 class="abs f-title" style="left:750px;top:3377px">CONTACT INFORMATION</h3>
  <div class="abs brand f-logo-name">VorentaMx</div>
  <p class="abs f-text" style="color:#ddd">Enter your email address to subscribe to this blog and receive notifications of new posts by email.</p>
  <div class="abs f-input" style="color:#ddd">E-mail address... <svg width="20" height="12" viewBox="0 0 20 12" fill="none" stroke="#ddd" stroke-width="1.6"><path d="M1 6h17M13 1l5 5-5 5"/></svg></div>
  <div class="abs contact" style="top:3455px;color:#ddd"><svg width="20" height="18" viewBox="0 0 20 18" fill="#ddd"><path d="M10 1L1 9h3v8h5v-5h2v5h5V9h3z"/></svg><span>218 Harrow Lane, Fairmount,<br>Philadelphia</span></div>
  <div class="abs contact" style="top:3524px;color:#ddd"><svg width="20" height="18" viewBox="0 0 20 18" fill="#ddd"><path d="M4 1l3 4-2 2c1 3 3 5 6 6l2-2 4 3-2 3C8 17 2 11 1 4z"/></svg><span>+1 215 555 0148</span></div>
  <div class="abs contact" style="top:3577px;color:#ddd"><svg width="20" height="16" viewBox="0 0 20 16" fill="#ddd"><path d="M1 2h18v1l-9 6-9-6zM1 5l9 6 9-6v10H1z"/></svg><span>office@vorentamx.com</span></div>
  <div class="abs social">
    <svg width="18" height="18"><circle cx="9" cy="9" r="7" fill="#ccc"/></svg>
    <svg width="18" height="18"><circle cx="9" cy="9" r="7" fill="#ccc"/></svg>
    <svg width="18" height="18"><circle cx="9" cy="9" r="7" fill="#ccc"/></svg>
    <svg width="18" height="18"><circle cx="9" cy="9" r="7" fill="#ccc"/></svg>
  </div>
  <div class="abs copyright" style="color:#ddd">© Copyright 2019 VorentaMx &nbsp; | &nbsp; ALL RIGHTS RESERVED &nbsp; | &nbsp; Terms of Use &amp; Privacy Policy</div>
</footer>

</body>
</html>
```